Brindle Gardenworks Business Card

An eye catching, yet simple business card that includes;

1. our logo
2. office phone - 5127730194
3. email - brindlegardenworks@mailnest.example
4. website - www.brindlegardenworks.example
5. instagram - @brindlegardenworksrvt

```html
<!DOCTYPE html>
<html lang="en">
<head>
<meta charset="utf-8">
<title>Brindle Gardenworks Business Card</title>
<link rel="stylesheet" href="https://fonts.googleapis.com/css2?family=Montserrat:wght@400;500;700;800&display=swap">
<style>
  :root {
    --brown: #9c5c28;
    --ink: #1c1a18;
    --paper: #ffffff;
    --stage: #e9e6e2;
  }
  * { box-sizing: border-box; margin: 0; padding: 0; }
  html, body { width: 1200px; height: 786px; overflow: hidden; }
  body {
    background: var(--stage);
    font-family: "Montserrat", sans-serif;
    position: relative;
  }
  .card {
    position: absolute;
    top: 243px;
    width: 525px;
    height: 300px;
    overflow: hidden;
    box-shadow: 0 6px 18px rgba(0,0,0,0.18);
  }
  .card-front { left: 50px; background: var(--paper); }
  .card-back { left: 625px; background: var(--brown); }

  .brand {
    position: absolute;
    display: flex;
    align-items: center;
    gap: 10px;
    font-weight: 800;
    letter-spacing: 0.5px;
  }
  .brand-dot { width: 18px; height: 18px; border-radius: 50%; flex: none; }
  .card-front .brand { top: 42px; right: 34px; color: var(--ink); font-size: 26px; }
  .card-front .brand-dot { background: var(--brown); }
  .card-back .brand { top: 50%; left: 50%; transform: translate(-50%, -50%); color: var(--paper); font-size: 34px; }
  .card-back .brand-dot { background: var(--paper); width: 22px; height: 22px; }

  .rule {
    position: absolute;
    top: 104px; left: 150px; right: 34px;
    height: 2px; background: var(--brown);
  }
  .person { position: absolute; left: 34px; top: 122px; }
  .person-name { color: var(--brown); font-weight: 700; font-size: 22px; }
  .person-role { color: var(--ink); font-size: 13px; margin-top: 2px; }
  .person-underline { width: 150px; height: 2px; background: var(--brown); margin-top: 6px; }

  .contacts { position: absolute; left: 34px; top: 190px; list-style: none; }
  .contacts li {
    display: flex; align-items: center; gap: 10px;
    font-size: 12.5px; color: var(--ink); height: 20px;
  }
  .contacts svg { width: 13px; height: 13px; flex: none; }

  .address {
    position: absolute; right: 34px; top: 190px;
    text-align: right; font-size: 12px; line-height: 1.35; color: var(--ink);
  }
  .band {
    position: absolute; left: 0; right: 0; bottom: 0;
    height: 16px; background: var(--brown);
  }
</style>
</head>
<body>
  <section class="card card-front">
    <div class="brand"><span class="brand-dot"></span>Brindle Gardenworks</div>
    <div class="rule"></div>
    <div class="person">
      <p class="person-name">Darren Holloway</p>
      <p class="person-role">Managing Director</p>
      <div class="person-underline"></div>
    </div>
    <ul class="contacts">
      <li>
        <svg viewBox="0 0 16 16"><path fill="#9c5c28" d="M3 1.5 6 1l1.5 3.5-2 1.3a9 9 0 0 0 4.7 4.7l1.3-2L15 10l-.5 3c-.2.8-1 1.3-1.8 1.2C6.8 13.5 2.5 9.2 1.8 3.3 1.7 2.5 2.2 1.7 3 1.5Z"/></svg>
        5127730194
      </li>
      <li>
        <svg viewBox="0 0 16 16"><rect x="1" y="3" width="14" height="10" rx="1" fill="#9c5c28"/><path d="M1.5 3.8 8 9l6.5-5.2" fill="none" stroke="#fff" stroke-width="1.3"/></svg>
        brindlegardenworks@mailnest.example
      </li>
      <li>
        <svg viewBox="0 0 16 16"><circle cx="8" cy="8" r="6.5" fill="none" stroke="#9c5c28" stroke-width="1.6"/><ellipse cx="8" cy="8" rx="2.8" ry="6.5" fill="none" stroke="#9c5c28" stroke-width="1.3"/><path d="M1.5 8h13" stroke="#9c5c28" stroke-width="1.3"/></svg>
        www.brindlegardenworks.example
      </li>
      <li>
        <svg viewBox="0 0 16 16"><circle cx="8" cy="8" r="6.5" fill="#9c5c28"/></svg>
        @brindlegardenworksrvt
      </li>
    </ul>
    <p class="address">48 Quarry Bend Road<br>Riverton, TX 78601</p>
    <div class="band"></div>
  </section>

  <section class="card card-back">
    <div class="brand"><span class="brand-dot"></span>Brindle Gardenworks</div>
  </section>
</body>
</html>
```